New business card for a regional office of a US M&A company

We need business card for a finance company, office based in Hong Kong , our Head office is in US, our business is to Merge and acquires companies , the new office will be a regional office for the Asia Pacific region. We want to use the head office logo as attached ( but don't have to be exactly the same, can be a variation to it) as a base and then add Asia Pacific alongside the logo.
We would prefer to have be bilingual Eng + Chinese, although we don't really have Chinese company name .

Industry/Entity Type

Business

Contact Information for Business Card

Carla Beth Soren
 

VP,
APAC M&A Operations
Tovar Crest Asia Pacific Limited
 
Unit 1407, K82
27 Sai Lok Fung Road, 
Hong Kong 
 
M: +852 6481 2037
T : +852 2736 4100
F : +852 2736 4155
VOIP: 4813
 
cbsoren@tovarcrest.com

Font styles to use
Serif
Sans Serif

Colors

Designer to choose colors to be used in the design.

Requirements
Must have
• APAC Office

```html
<!DOCTYPE html>
<html lang="en">
<head>
<meta charset="utf-8">
<title>Tovar Crest Asia Pacific – Business Card</title>
<link rel="stylesheet" href="https://fonts.googleapis.com/css2?family=Noto+Sans+TC:wght@400;500&family=Open+Sans:wght@400;600;700;800&display=swap">
<style>
  :root {
    --teal: #00a9c8;
    --navy: #10294a;
    --ink: #3c4a5a;
    --paper: #ffffff;
    --backdrop: #d6d8da;
  }
  * { box-sizing: border-box; margin: 0; padding: 0; }
  html, body {
    width: 1200px; height: 800px; overflow: hidden;
    background: var(--backdrop);
    font-family: "Open Sans", Arial, sans-serif;
  }
  .zh { font-family: "Noto Sans TC", "Open Sans", sans-serif; }
  .sheet {
    width: 1200px; height: 800px;
    display: flex; align-items: center; justify-content: center; gap: 50px;
  }
  .card {
    position: relative;
    width: 540px; height: 310px;
    overflow: hidden;
    box-shadow: 0 6px 18px rgba(0,0,0,.18);
  }

  /* ---------- front ---------- */
  .card--front { background: var(--paper); color: var(--navy); }
  .front__brand {
    position: absolute; top: 24px; right: 40px;
    font-weight: 800; font-size: 30px; line-height: 36px; letter-spacing: 1px;
    color: var(--teal);
  }
  .front__region {
    position: absolute; top: 62px; right: 40px;
    font-weight: 600; font-size: 11px; line-height: 14px; letter-spacing: 2px;
    color: var(--navy);
  }
  .front__region .zh { letter-spacing: 1px; font-weight: 500; margin-left: 6px; }
  .front__mark {
    position: absolute; top: 92px; right: 40px;
    width: 100px; height: 100px;
    background: var(--navy);
  }
  .front__accent {
    position: absolute; left: 0; top: 92px;
    width: 7px; height: 40px; background: var(--teal);
  }
  .person { position: absolute; left: 34px; top: 90px; }
  .person__name {
    font-weight: 600; font-size: 19px; line-height: 24px; letter-spacing: .5px;
    text-transform: uppercase; color: var(--navy);
  }
  .person__title { font-size: 12.5px; line-height: 17px; color: var(--ink); }
  .person__company { font-size: 11px; line-height: 15px; color: var(--ink); margin-top: 2px; }
  .person__title-zh { font-size: 11px; line-height: 16px; color: var(--ink); }

  .contact { position: absolute; left: 34px; top: 172px; font-size: 11.5px; color: var(--ink); }
  .contact__voip { font-weight: 700; color: var(--navy); font-size: 12px; line-height: 16px; margin-bottom: 4px; }
  .contact__list { list-style: none; }
  .contact__item { display: flex; align-items: center; gap: 8px; line-height: 15px; }
  .contact__icon { width: 10px; height: 10px; flex: none; }
  .contact__address { margin-top: 6px; line-height: 15px; }

  .front__band { position: absolute; left: 0; bottom: 0; width: 540px; height: 40px; }

  /* ---------- back ---------- */
  .card--back {
    background: var(--teal); color: var(--paper);
    display: flex; flex-direction: column; align-items: center; justify-content: center;
  }
  .back__mark { width: 58px; height: 58px; background: var(--paper); margin-bottom: 16px; }
  .back__brand { font-weight: 800; font-size: 40px; line-height: 48px; letter-spacing: 1.5px; }
  .back__region { font-weight: 600; font-size: 13px; line-height: 18px; letter-spacing: 3px; margin-top: 4px; }
  .back__region .zh { letter-spacing: 2px; font-weight: 500; margin-left: 8px; }
</style>
</head>
<body>
<main class="sheet">

  <section class="card card--front" aria-label="Business card front">
    <div class="front__brand">TOVAR CREST</div>
    <div class="front__region">ASIA PACIFIC<span class="zh" lang="zh-Hant">亞太區</span></div>
    <div class="front__mark" aria-hidden="true"></div>
    <div class="front__accent" aria-hidden="true"></div>

    <div class="person">
      <div class="person__name">Carla Beth Soren</div>
      <div class="person__title">VP, APAC M&amp;A Operations</div>
      <div class="person__title-zh zh" lang="zh-Hant">亞太區併購營運副總裁</div>
      <div class="person__company">Tovar Crest Asia Pacific Limited</div>
    </div>

    <div class="contact">
      <div class="contact__voip">VOIP: 4813</div>
      <ul class="contact__list">
        <li class="contact__item">
          <svg class="contact__icon" viewBox="0 0 10 10" aria-label="Mobile"><rect x="2.5" y="0.5" width="5" height="9" rx="1" fill="none" stroke="#00a9c8" stroke-width="1"/></svg>
          +852 6481 2037
        </li>
        <li class="contact__item">
          <svg class="contact__icon" viewBox="0 0 10 10" aria-label="Telephone"><path d="M2 1 L4 1 L4.5 3 L3.3 4 Q4.5 6.2 6 6.7 L7 5.5 L9 6 L9 8 Q5 9.5 1 4 Z" fill="#00a9c8"/></svg>
          +852 2736 4100
        </li>
        <li class="contact__item">
          <svg class="contact__icon" viewBox="0 0 10 10" aria-label="Fax"><rect x="2.5" y="0.5" width="5" height="3" fill="#00a9c8"/><rect x="0.5" y="4" width="9" height="5" rx="1" fill="#00a9c8"/></svg>
          +852 2736 4155
        </li>
        <li class="contact__item">
          <svg class="contact__icon" viewBox="0 0 10 10" aria-label="Email"><rect x="0.5" y="2" width="9" height="6.5" fill="#00a9c8"/><path d="M0.5 2 L5 5.5 L9.5 2" fill="none" stroke="#fff" stroke-width="1"/></svg>
          cbsoren@tovarcrest.com
        </li>
      </ul>
      <div class="contact__address">Unit 1407, K82 27 Sai Lok<br>Fung Road, Hong Kong</div>
    </div>

    <svg class="front__band" viewBox="0 0 540 40" preserveAspectRatio="none" aria-hidden="true">
      <polygon points="340,22 540,10 540,16 340,28" fill="#00a9c8"/>
      <polygon points="250,40 340,26 540,14 540,40" fill="#10294a"/>
    </svg>
  </section>

  <section class="card card--back" aria-label="Business card back">
    <div class="back__mark" aria-hidden="true"></div>
    <div class="back__brand">TOVAR CREST</div>
    <div class="back__region">ASIA PACIFIC<span class="zh" lang="zh-Hant">亞太區</span></div>
  </section>

</main>
</body>
</html>
```